Brightvale Real Estate

We are looking for help with web design for a new company that is revolutionizing the real estate world on the listing side: by charing per hour for top level professional real estate services. We would like the concept to be simple, clean and easily understood.
Updates

We want this website to actually function, not just a static design.

Industry/Entity Type

Real Estate

```html
<!DOCTYPE html>
<html lang="en">
<head>
<meta charset="utf-8">
<title>Brightvale Real Estate</title>
<link href="https://fonts.googleapis.com/css2?family=Roboto+Condensed:wght@400;700&family=Roboto:wght@300;400;500;700&display=swap" rel="stylesheet">
<style>
:root{
  --teal:#1fcca6;
  --navy:#2d3b4e;
  --navy-deep:#263244;
  --ink:#2b3746;
  --muted:#8a939e;
  --line:#e3e6ea;
  --white:#ffffff;
  --band:#5a5f66;
}
*{margin:0;padding:0;box-sizing:border-box}
html,body{width:682px;height:1200px;overflow:hidden;background:var(--white)}
body{position:relative;font-family:"Roboto",Arial,sans-serif;color:var(--ink)}
.abs{position:absolute}
a{color:inherit;text-decoration:none}

/* top bar */
.topbar{left:0;top:0;width:682px;height:15px;background:var(--navy-deep);color:#d8dde3;font-size:6.5px}
.topbar span{position:absolute;top:4px;white-space:nowrap}
.topbar .reg{color:var(--teal)}
.topbar .dot{width:7px;height:7px;border-radius:50%;background:#d8dde3;top:4px}
.ico{display:inline-block;width:5px;height:5px;border-radius:50%;background:#d8dde3;margin-right:3px;vertical-align:0}

/* nav */
.nav{left:0;top:15px;width:682px;height:38px;background:var(--white);border-bottom:1px solid var(--line)}
.nav a{position:absolute;top:12px;font-family:"Roboto Condensed",sans-serif;font-size:13.5px;color:#4a5562;letter-spacing:.2px}
.nav a.active{color:var(--teal)}

/* hero */
.hero{left:0;top:53px;width:682px;height:279px;background:radial-gradient(ellipse at 60% 35%,#3c4e63 0%,#243244 55%,#18212d 100%)}
.brandmark{left:0;width:682px;top:70px;text-align:center;color:#fff;font-family:"Roboto Condensed",sans-serif;font-weight:700;font-size:14px;letter-spacing:3px;text-transform:uppercase}
.brandmark i{display:inline-block;width:10px;height:10px;border-radius:50%;background:#fff;margin-right:8px;vertical-align:-1px}
.hero h1{left:0;width:682px;top:170px;text-align:center;font-family:"Roboto Condensed",sans-serif;font-weight:700;font-size:32px;color:#fff;letter-spacing:.3px}
.hero .tag{left:0;width:682px;top:207px;text-align:center;font-size:10.5px;color:#fff}
.btn{top:241px;height:23px;line-height:21px;font-family:"Roboto Condensed",sans-serif;font-weight:700;font-size:9px;text-align:center;color:#fff;text-transform:uppercase}
.btn-map{left:259px;width:89px;background:var(--teal);border:1px solid var(--teal)}
.btn-info{left:359px;width:64px;border:1px solid #fff}
.arrow-l{left:0;top:124px;width:31px;height:31px;background:rgba(255,255,255,.15)}
.arrow-r{left:650px;top:124px;width:32px;height:31px;background:var(--teal)}

/* search band */
.searchband{left:0;top:332px;width:682px;height:42px;background:var(--band)}
.search{left:234px;top:10px;width:196px;height:21px;background:#fff;font-size:11px;color:#9aa2ab;padding:4px 8px}
.search-btn{left:430px;top:10px;width:27px;height:21px;background:var(--teal)}

/* featured */
.sec-title{left:0;width:682px;text-align:center;font-family:"Roboto Condensed",sans-serif;font-weight:700}
.featured-title{top:394px;font-size:25px;color:var(--ink)}
.featured-sub{top:422px;font-size:10.5px;color:#4a5562;font-family:"Roboto",sans-serif;font-weight:400}
.card{top:468px;width:110px;height:100px;background:#f1f2f4;border:1px solid #e2e5e8}
.card .photo{height:77px}
.card .cap{padding:3px 6px;font-size:6.5px;color:#4a5562;line-height:1.25}
.card .cap small{display:block;font-size:5.5px;color:#6d7680}
.card .chev{position:absolute;right:7px;bottom:7px}
.card.faded{opacity:.55}
.card.active{top:454px;width:111px;height:122px;border:2px solid var(--teal);background:var(--navy)}
.card.active .photo{height:90px}
.card.active .cap{color:#fff;padding-top:6px}
.card.active .cap small{color:#b8c0c9}

/* holidays */
.holidays{left:0;top:628px;width:682px;height:208px;background:linear-gradient(180deg,#46576b 0%,#33445a 100%)}
.holidays h2{top:33px;font-size:11.5px;color:#fff}
.holidays .sub{top:49px;font-size:6.5px;color:#b7c0ca;font-family:"Roboto",sans-serif;font-weight:400}
.htype{top:82px;width:64px;margin-left:-32px;text-align:center}
.htype .ring{width:62px;height:62px;border-radius:50%;border:2px solid #fff;margin:0 auto;display:flex;align-items:center;justify-content:center}
.htype p{margin-top:9px;font-size:8.5px;color:#c6cdd5}
.htype.active .ring{border-color:var(--teal);background:rgba(31,204,166,.12)}
.htype.active p{color:var(--teal)}

/* clients */
.clients-title{top:863px;font-size:11.5px;color:var(--ink)}
.clients-sub{top:878px;font-size:6.5px;color:#4a5562;font-family:"Roboto",sans-serif;font-weight:400}
.quote{top:906px;width:189px;height:56px;border:1px solid #eceef1;background:#fff;padding:8px 8px;font-size:6.5px;color:#a3abb4;line-height:1.3}
.quote .who{color:var(--teal);font-size:8px;margin-top:2px;opacity:.55}
.quote .where{font-size:5px;color:#c0c6cc}
.quote.active{border-top:2px solid var(--teal);color:var(--ink)}
.quote.active .who{opacity:1}
.quote .tail{position:absolute;bottom:-8px;right:22px;width:0;height:0;border-left:8px solid transparent;border-top:8px solid #eceef1}

/* footer */
.footer{left:0;top:1020px;width:682px;height:118px;background:var(--navy)}
.fcol{top:25px}
.fcol h3{font-size:11px;font-weight:500;color:var(--teal);margin-bottom:6px}
.fcol p{font-size:5.5px;color:#d5dbe2;line-height:1.45}
.nl-input{width:58px;height:11px;background:#fff;font-size:5px;color:#777;padding:2px 4px;display:inline-block}
.nl-go{display:inline-block;width:19px;height:11px;background:var(--teal);color:#fff;font-size:5.5px;text-align:center;line-height:11px;margin-left:3px}
.news{display:flex;gap:6px;margin-bottom:6px;width:100px}
.news .thumb{width:14px;height:14px;background:linear-gradient(135deg,#7a8797,#3d4a5a);flex:none}
.news b{font-weight:400;font-size:5.5px;color:#fff;display:block;line-height:1.4}
.news em{font-style:normal;font-size:4.8px;color:var(--teal)}
.tags{width:92px;display:flex;flex-wrap:wrap;gap:3px}
.tags span{border:1px solid #aeb7c1;color:#e5e9ee;font-size:5px;padding:2px 3px}
.social{display:flex;gap:12px;margin-top:6px}
.social i{width:7px;height:7px;border-radius:50%;background:#fff;display:block}

.bottombar{left:0;top:1138px;width:682px;height:62px;background:var(--navy-deep);border-top:1px solid #3a485a}
.fnav{left:0;width:682px;top:14px;text-align:center;font-size:6px;color:#d5dbe2}
.fnav .on{color:var(--teal)}
.copy{left:0;width:682px;top:26px;text-align:center;font-size:5px;color:#8e99a6}
.totop{left:333px;top:48px}
</style>
</head>
<body>

<div class="abs topbar">
  <span style="left:108px"><i class="ico"></i>Agent Login</span>
  <span style="left:161px"><i class="ico"></i>Customer Login</span>
  <span style="left:225px"><i class="ico"></i>Not a Member ? <a class="reg" href="#">Register</a></span>
  <span style="left:312px">Call Us Now :555-210-3384</span>
  <i class="abs dot" style="left:508px"></i>
  <i class="abs dot" style="left:527px"></i>
  <i class="abs dot" style="left:546px"></i>
  <i class="abs dot" style="left:563px"></i>
</div>

<nav class="abs nav">
  <a class="active" href="#" style="left:132px">HOME</a>
  <a href="#" style="left:197px">BUYING</a>
  <a href="#" style="left:272px">PRESS</a>
  <a href="#" style="left:341px">SELLING</a>
  <a href="#" style="left:420px">CAREERS</a>
  <a href="#" style="left:500px">ABOUT US</a>
</nav>

<section class="abs hero" role="img" aria-label="Night skyline of a large city with lit towers">
  <div class="abs brandmark"><i></i>Brightvale Real Estate</div>
  <h1 class="abs">BRIGHTVALE REAL ESTATE</h1>
  <p class="abs tag">You Don't Need Magic to Disappear. All you need is a destination.</p>
  <a class="abs btn btn-map" href="#">Show on the map</a>
  <a class="abs btn btn-info" href="#">More info</a>
  <a class="abs arrow-l" href="#" aria-label="Previous"><svg width="31" height="31"><path d="M18 10l-6 5.5 6 5.5" fill="none" stroke="#fff" stroke-width="1.5"/></svg></a>
  <a class="abs arrow-r" href="#" aria-label="Next"><svg width="32" height="31"><path d="M13 10l6 5.5-6 5.5" fill="none" stroke="#fff" stroke-width="2"/></svg></a>
</section>

<div class="abs searchband">
  <div class="abs search">Search your properties</div>
  <a class="abs search-btn" href="#" aria-label="Search"><svg width="27" height="21"><circle cx="12.5" cy="9.5" r="5" fill="none" stroke="#fff" stroke-width="2"/><path d="M16 13l4 4" stroke="#fff" stroke-width="2.5" stroke-linecap="round"/></svg></a>
</div>

<h2 class="abs sec-title featured-title">FEATURED PROPERTY</h2>
<p class="abs sec-title featured-sub">Best 2015 packages where people love to stay!</p>

<div class="abs card faded" style="left:-11px">
  <div class="photo" role="img" aria-label="White house with porch and green lawn" style="background:linear-gradient(180deg,#c9d8e6,#a9b6a0 60%,#7fa062)"></div>
  <div class="cap">Statue of liberty - USA<small>New Destination!</small></div>
</div>
<div class="abs card" style="left:106px">
  <div class="photo" role="img" aria-label="White two-storey house with dark roof" style="background:linear-gradient(180deg,#cfe0f0,#e6e6e0 55%,#7d9a5a)"></div>
  <div class="cap">Spectacular Seychelles<small>New Destination!</small></div>
  <svg class="chev" width="8" height="5"><path d="M1 1l3 3 3-3" fill="none" stroke="#8a939e"/></svg>
</div>
<div class="abs card active" style="left:226px">
  <div class="photo" role="img" aria-label="Modern villa lit at dusk with pool" style="background:linear-gradient(180deg,#3a3226,#c07a2a 55%,#4d7f6a)"></div>
  <div class="cap">Hong Kong &amp; Macau<small>Bonus Extras!</small></div>
  <svg class="chev" width="8" height="5"><path d="M1 1l3 3 3-3" fill="none" stroke="#fff"/></svg>
</div>
<div class="abs card" style="left:346px">
  <div class="photo" role="img" aria-label="Row of brick town houses along a street" style="background:linear-gradient(180deg,#b9d3ee,#a8755a 55%,#8a8f8a)"></div>
  <div class="cap">Vietnam Highlights<small>New Destination!</small></div>
  <svg class="chev" width="8" height="5"><path d="M1 1l3 3 3-3" fill="none" stroke="#8a939e"/></svg>
</div>
<div class="abs card" style="left:465px">
  <div class="photo" role="img" aria-label="Modern apartment block with garden" style="background:linear-gradient(180deg,#d7e6f3,#d8d3c6 55%,#6f9a4f)"></div>
  <div class="cap">Spectacular Seychelles<small>New Destination!</small></div>
  <svg class="chev" width="8" height="5"><path d="M1 1l3 3 3-3" fill="none" stroke="#8a939e"/></svg>
</div>
<div class="abs card faded" style="left:584px">
  <div class="photo" role="img" aria-label="Large white family house" style="background:linear-gradient(180deg,#d6e3ee,#e4e2dc 55%,#8aa670)"></div>
  <div class="cap">Dubai<small>New Destination!</small></div>
</div>

<section class="abs holidays" role="img" aria-label="Faded city waterfront behind holiday categories">
  <h2 class="abs sec-title">HOLIDAYS TYPE</h2>
  <p class="abs sec-title sub">get explore your dream to travel the world!</p>

  <div class="abs htype" style="left:144px"><div class="ring"><svg width="30" height="30" viewBox="0 0 30 30" fill="#fff"><rect x="12" y="4" width="5" height="5"/><rect x="8" y="9" width="14" height="6"/><path d="M3 15h24l-4 8H7z"/><path d="M2 26q4-2 7 0t7 0 7 0 5 0" stroke="#fff" fill="none" stroke-width="1.5"/></svg></div><p>Cruise</p></div>
  <div class="abs htype" style="left:223px"><div class="ring"><svg width="30" height="30" viewBox="0 0 30 30" fill="#fff"><rect x="5" y="11" width="7" height="16"/><rect x="13" y="4" width="7" height="23"/><rect x="21" y="14" width="5" height="13"/></svg></div><p>City Breaks</p></div>
  <div class="abs htype active" style="left:301px"><div class="ring"><svg width="34" height="24" viewBox="0 0 34 24" fill="var(--teal)"><path d="M11 22C4 17 1 13 1 8a5 5 0 0 1 10-1 5 5 0 0 1 10 1c0 5-3 9-10 14z"/><path d="M23 22c-4-3-6-6-6-9a4.5 4.5 0 0 1 9-1 4.5 4.5 0 0 1 7 3c0 3-3 5-10 7z"/></svg></div><p>Honeymoon</p></div>
  <div class="abs htype" style="left:380px"><div class="ring"><svg width="32" height="32" viewBox="0 0 32 32"><circle cx="16" cy="16" r="11" fill="none" stroke="#fff" stroke-width="2"/><path d="M22 10l-4 8-8 4 4-8z" fill="#fff"/></svg></div><p>Adventure</p></div>
  <div class="abs htype" style="left:459px"><div class="ring"><svg width="30" height="30" viewBox="0 0 30 30" fill="#fff"><path d="M14 10q2 8-2 18h3q3-10 1-18z"/><path d="M15 10Q8 4 3 9q6-2 12 1zM15 10q6-7 12-2-6-1-12 2zM15 10q-3 3-4 9 0-6 4-9zM15 10q5 2 6 8-2-5-6-8z"/><rect x="6" y="27" width="18" height="2"/></svg></div><p>Safari</p></div>
  <div class="abs htype" style="left:536px"><div class="ring"><svg width="34" height="22" viewBox="0 0 34 22" fill="#fff"><path d="M2 13h30l-5 6H7z"/><path d="M10 13l4-5h10l3 5z"/><path d="M2 21q4-2 8 0t8 0 8 0" stroke="#fff" fill="none"/></svg></div><p>Beach</p></div>
</section>

<h2 class="abs sec-title clients-title">HAPPY CLIENTS</h2>
<p class="abs sec-title clients-sub">what customer say about us and why love our services!</p>

<div class="abs quote" style="left:-114px">Lorem Ipsum is simply dummy text of the printing and typese tting industry. Lorem Ipsum has been the industry's.<div class="who">Client Name</div><div class="where">United States</div><span class="tail"></span></div>
<div class="abs quote" style="left:83px">Lorem Ipsum is simply dummy text of the printing and typese tting industry. Lorem Ipsum has been the industry's.<div class="who">Client Name</div><div class="where">United States</div><span class="tail"></span></div>
<div class="abs quote active" style="left:277px">Lorem Ipsum is simply dummy text of the printing and typeset industry. Lorem Ipsum has been the industry's standard dummy text ever hen an with new version look.<div class="who">Client Name</div><div class="where">United States</div><span class="tail"></span></div>
<div class="abs quote" style="left:474px">Lorem Ipsum is simply dummy text of the printing and typeset- ting industry. Lorem Ipsum has been the industry's.<div class="who">Client Name</div><div class="where">United States</div><span class="tail"></span></div>
<div class="abs quote" style="left:670px">Lorem Ipsum is simply dummy text.<div class="who">Client Name</div><div class="where">United States</div></div>

<footer class="abs footer">
  <div class="abs fcol" style="left:105px;width:95px">
    <h3>Newsletter</h3>
    <p>Duis autem vel eum iriure dolor in hendrerit in vulputate velit esse molestie consequat, vel illum dolore.</p>
    <div style="margin-top:6px"><span class="nl-input">Subscribes...</span><span class="nl-go">GO</span></div>
  </div>
  <div class="abs fcol" style="left:222px">
    <h3>Latest News</h3>
    <div class="news"><div class="thumb" role="img" aria-label="Gallery thumbnail"></div><div><b>Postformat Gallery: Multiple images</b><em>April 21, 2015 - 3:01 pm</em></div></div>
    <div class="news"><div class="thumb" role="img" aria-label="Snowboarding thumbnail"></div><div><b>Snowboarding is fun!</b><em>March 10, 2015 - 5:11 pm</em></div></div>
  </div>
  <div class="abs fcol" style="left:340px">
    <h3>Tags</h3>
    <div class="tags"><span>Agent Login</span><span>Customer Login</span><span>Not a Member?</span><span>Contact</span><span>New Horizons</span><span>Lanscape</span><span>Tags</span><span>Nice</span><span>Some</span><span>Portrait</span></div>
  </div>
  <div class="abs fcol" style="left:458px">
    <h3>Address</h3>
    <p>Brightvale Real Estate</p>
    <p style="margin-top:3px">42b, 20871 Harborview, USA</p>
    <p style="margin-top:3px"><span style="color:var(--teal)">E-mail:</span> info@brightvalerealestate.com</p>
    <div class="social"><i></i><i></i><i></i><i></i></div>
  </div>
</footer>

<div class="abs bottombar">
  <p class="abs fnav"><span class="on">Home</span> &nbsp;::&nbsp; Destinations &nbsp;::&nbsp; Criuses &nbsp;::&nbsp; Specils &nbsp;::&nbsp; Holidays &nbsp;::&nbsp; Blog &nbsp;::&nbsp; Contact Us</p>
  <p class="abs copy">Copyright | 2015 - Brightvale Real Estate . All Right Reserved.</p>
  <svg class="abs totop" width="30" height="14"><path d="M0 14L15 0l15 14z" fill="var(--teal)"/><path d="M11 10l4-4 4 4" fill="none" stroke="#fff" stroke-width="1.5"/></svg>
</div>

</body>
</html>
```